Security and Automation Company based in Texas and needs logo design also

Looking for a new logo design for our company - we are based in Texas and specialize in camera, security and home automation - We do want the main company name(Brightline Guard and Controls of Texas) with our parent company in small letters below (a Veloran Partners, LLC Company) and our License number needs to be included in the design - K74836 - Darker shades of blue preferred

Target Market(s)

We work with everyone from home to large corporate - so clean design would be helpful

Industry/Entity Type

It Company

Contact Information for Business Card

PO Box 4719
Cedar Hollow, Texas 75961
Leave a spot for the phone number and email address

Logo Text

Brightline Guard and Controls of Texas/a Veloran Partners Company/K74836

Font styles to use
Sans Serif

Colors
0255a3

```html
<!DOCTYPE html>
<html lang="en">
<head>
<meta charset="utf-8">
<title>Brightline Guard and Controls of Texas – Business Card</title>
<link rel="stylesheet" href="https://fonts.googleapis.com/css2?family=Arimo:wght@700&display=swap">
<style>
  :root {
    --card-dark: #1b1b1b;
    --card-mid: #262626;
    --brand-blue: #0255a3;
    --brand-blue-light: #1f6fc4;
    --text-white: #ffffff;
  }
  html, body {
    margin: 0;
    padding: 0;
    width: 1200px;
    height: 754px;
    overflow: hidden;
    background: var(--card-dark);
  }
  .card {
    position: relative;
    width: 1200px;
    height: 754px;
    overflow: hidden;
    font-family: "Arimo", Arial, sans-serif;
  }
  .card__texture {
    position: absolute;
    inset: 0;
    background: radial-gradient(ellipse at 55% 40%, var(--card-mid) 0%, var(--card-dark) 75%);
  }
  .card__brand {
    position: absolute;
    top: 44px;
    right: 44px;
    width: 360px;
    display: flex;
    align-items: center;
    gap: 14px;
  }
  .card__brand-mark {
    flex: 0 0 auto;
    width: 34px;
    height: 34px;
    background: var(--brand-blue-light);
  }
  .card__brand-name {
    margin: 0;
    color: var(--brand-blue-light);
    font-weight: 700;
    font-size: 30px;
    line-height: 1.1;
  }
  .card__contact {
    position: absolute;
    left: 51px;
    top: 256px;
    margin: 0;
    color: var(--text-white);
    font-style: normal;
    font-weight: 700;
    font-size: 37px;
    line-height: 48px;
  }
  .card__contact span { display: block; }
  .card__band {
    position: absolute;
    left: 0;
    right: 0;
    bottom: 0;
    height: 91px;
    background: var(--brand-blue);
  }
</style>
</head>
<body>
  <main class="card">
    <div class="card__texture" role="img" aria-label="Dark charcoal background with a subtle grid of square tiles"></div>

    <div class="card__brand">
      <span class="card__brand-mark"></span>
      <p class="card__brand-name">Brightline Guard and Controls of Texas</p>
    </div>

    <address class="card__contact">
      <span class="card__contact-name">Name</span>
      <span class="card__contact-box">P. O .Box 4719</span>
      <span class="card__contact-city">Cedar Hollow, Texas 75961</span>
      <span class="card__contact-phone">Phone Number</span>
      <span class="card__contact-email">E-mail Address</span>
    </address>

    <div class="card__band"></div>
  </main>
</body>
</html>
```